i need a business card design for my family investment company "varundel investments" based in dubai. its a diverse investment firm focusing on education, hospitality and automotive. the design has to be modern and try to incorporate the logo "E" in the design. details on card as follow

Yousef R Bin Hadrami
Managing Director
yousef@varundel.ae
www.varundel.ae

Harbor zone,falcon tower, office 3817, dubai
tel. 04 7391852
mobile.050 8142903

Target Market(s)

card used for networking events and investor meetings

Industry/Entity Type

Hospitality

```html
<!DOCTYPE html>
<html lang="en">
<head>
<meta charset="utf-8">
<title>Varundel Investments — Business Card</title>
<link rel="stylesheet" href="https://fonts.googleapis.com/css2?family=Questrial&display=swap">
<style>
  :root {
    --backdrop: #3b3b3d;
    --card: #ffffff;
    --band: #5e7eab;
    --ink: #161616;
    --on-band: #ffffff;
    --accent-text: #5e7eab;
    --card-w: 520px;
    --card-h: 300px;
  }
  * { box-sizing: border-box; margin: 0; padding: 0; }
  html, body {
    width: 1200px; height: 720px; overflow: hidden;
    background: var(--backdrop);
    font-family: "Questrial", sans-serif;
  }
  .stage {
    position: relative; width: 1200px; height: 720px;
    display: flex; align-items: center; justify-content: center; gap: 60px;
  }
  .card {
    position: relative; width: var(--card-w); height: var(--card-h);
    background: var(--card); overflow: hidden;
    box-shadow: 0 10px 28px rgba(0,0,0,.35);
  }
  .card__bands { position: absolute; inset: 0; width: 100%; height: 100%; }
  .card__bands .band { fill: var(--band); }
  .card__bands .band-stroke { fill: none; stroke: var(--band); stroke-width: 17; }

  /* Front */
  .brand__name {
    position: absolute; left: 0; right: 0; top: 44px;
    text-align: center; color: var(--ink);
    font-size: 50px; line-height: 1; letter-spacing: 12px; padding-left: 12px;
  }
  .brand__sub {
    position: absolute; left: 0; right: 0; top: 124px; height: 22px;
    display: flex; align-items: center; justify-content: center;
    color: var(--on-band); font-size: 13px; letter-spacing: 14px; padding-left: 14px;
  }

  /* Back */
  .contact {
    position: absolute; right: 30px; top: 98px;
    text-align: right; color: var(--ink);
  }
  .contact__name  { font-size: 21px; }
  .contact__title { font-size: 14px; margin-top: 3px; }
  .contact__list  { list-style: none; margin-top: 16px; }
  .contact__item  {
    display: flex; justify-content: flex-end; align-items: center; gap: 7px;
    font-size: 14px; line-height: 22px;
  }
  .icon { width: 13px; height: 13px; flex: none; }
  .icon rect, .icon circle.solid, .icon path.solid { fill: var(--band); }
  .icon .hole { fill: #fff; }
  .address {
    position: absolute; left: 0; right: 30px; bottom: 20px;
    display: flex; justify-content: flex-end; align-items: center; gap: 7px;
    font-size: 14px; color: var(--accent-text);
  }
</style>
</head>
<body>
<main class="stage">

  <section class="card card--front" aria-label="Card front">
    <svg class="card__bands" viewBox="0 0 520 300" aria-hidden="true">
      <rect class="band" x="0" y="124" width="520" height="22"/>
      <rect class="band" x="0" y="166" width="520" height="22"/>
      <rect class="band" x="0" y="208" width="520" height="22"/>
    </svg>
    <p class="brand__name">VARUNDEL</p>
    <p class="brand__sub">INVESTMENTS</p>
  </section>

  <section class="card card--back" aria-label="Card back">
    <svg class="card__bands" viewBox="0 0 520 300" aria-hidden="true">
      <path class="band-stroke" d="M0,22 Q150,12 300,0"/>
      <path class="band-stroke" d="M0,55 Q170,32 330,-10"/>
      <path class="band-stroke" d="M0,88 Q190,55 380,-10"/>
    </svg>

    <div class="contact">
      <p class="contact__name">Yousef R Bin Hadrami</p>
      <p class="contact__title">Managing Director</p>
      <ul class="contact__list">
        <li class="contact__item">yousef@varundel.ae
          <svg class="icon" viewBox="0 0 13 13" aria-hidden="true"><rect x="0" y="2" width="13" height="9" rx="1"/><path d="M1 3 L6.5 7.5 L12 3" fill="none" stroke="#fff" stroke-width="1.2"/></svg>
        </li>
        <li class="contact__item">04 7391852
          <svg class="icon" viewBox="0 0 13 13" aria-hidden="true"><path class="solid" d="M1 4 Q6.5 0 12 4 L10.5 6 L8.5 5 L8.5 4 Q6.5 3.3 4.5 4 L4.5 5 L2.5 6 Z M3 7 H10 L11 12 H2 Z"/></svg>
        </li>
        <li class="contact__item">050 8142903
          <svg class="icon" viewBox="0 0 13 13" aria-hidden="true"><rect x="3" y="0" width="7" height="13" rx="1.2"/><rect class="hole" x="4.2" y="1.6" width="4.6" height="8" style="fill:#fff"/></svg>
        </li>
        <li class="contact__item">www.varundel.ae
          <svg class="icon" viewBox="0 0 13 13" aria-hidden="true"><circle class="solid" cx="6.5" cy="6.5" r="6.5"/><path d="M0.5 6.5 H12.5 M6.5 0.5 Q3 6.5 6.5 12.5 M6.5 0.5 Q10 6.5 6.5 12.5" fill="none" stroke="#fff" stroke-width="0.9"/></svg>
        </li>
      </ul>
    </div>

    <p class="address">Harbor zone,falcon tower, office 3817, dubai
      <svg class="icon" viewBox="0 0 13 13" aria-hidden="true"><path class="solid" d="M6.5 0 A4.5 4.5 0 0 1 11 4.5 Q11 7.5 6.5 13 Q2 7.5 2 4.5 A4.5 4.5 0 0 1 6.5 0 Z"/><circle class="hole" cx="6.5" cy="4.5" r="1.7"/></svg>
    </p>
  </section>

</main>
</body>
</html>
```